Book Cover Design

Design with title UNWAVERING
Subtitle: Ways to Kindle the Spark of Resolve
Author Name: Carla Jean Morrow
Put DAILY MERIDIAN BESTSELLER at top
Shimmer design, see inspirational images attached

```html
<!DOCTYPE html>
<html lang="en">
<head>
<meta charset="utf-8">
<title>Unwavering – Book Cover Spread</title>
<link rel="stylesheet" href="https://fonts.googleapis.com/css2?family=Archivo:wght@600;700;800&family=Tinos&family=Open+Sans:wght@400&display=swap">
<style>
  :root {
    --page-bg: #ffffff;
    --title-violet: #6a12e0;
    --spine-author-blue: #2a12d4;
    --ink-black: #0b0b0f;
    --text-white: #ffffff;
    --teal: #6cc6b8;
    --mint: #9fe6c8;
    --pink: #f49be0;
    --rose: #eeb0d8;
    --lilac: #b58ef0;
    --periwinkle: #8f9cf2;
    --cyan: #86e0ea;
    --sky: #a9c8f6;
    --lemon: #eef7c6;
    --mauve-grey: #b3a6b4;
    --peach: #f0c0b0;
  }
  html, body {
    margin: 0;
    padding: 0;
    width: 1111px;
    height: 1200px;
    overflow: hidden;
    background: var(--page-bg);
  }
  .cover-spread {
    position: absolute;
    left: 26px;
    top: 206px;
    width: 1058px;
    height: 787px;
    overflow: hidden;
    background:
      radial-gradient(ellipse 260px 150px at 130px 60px, var(--teal) 0%, rgba(108,198,184,0) 100%),
      radial-gradient(ellipse 200px 140px at 280px 120px, var(--mint) 0%, rgba(159,230,200,0) 100%),
      radial-gradient(ellipse 220px 280px at 40px 330px, var(--lilac) 0%, rgba(181,142,240,0) 100%),
      radial-gradient(ellipse 300px 200px at 250px 560px, var(--pink) 0%, rgba(244,155,224,0) 100%),
      radial-gradient(ellipse 230px 200px at 60px 720px, var(--periwinkle) 0%, rgba(143,156,242,0) 100%),
      radial-gradient(ellipse 200px 160px at 520px 80px, var(--pink) 0%, rgba(244,155,224,0) 100%),
      radial-gradient(ellipse 260px 220px at 720px 160px, var(--sky) 0%, rgba(169,200,246,0) 100%),
      radial-gradient(ellipse 180px 160px at 1030px 40px, var(--lemon) 0%, rgba(238,247,198,0) 100%),
      radial-gradient(ellipse 280px 150px at 830px 360px, var(--cyan) 0%, rgba(134,224,234,0) 100%),
      radial-gradient(ellipse 260px 240px at 980px 600px, var(--mauve-grey) 0%, rgba(179,166,180,0) 100%),
      radial-gradient(ellipse 180px 120px at 1050px 780px, var(--peach) 0%, rgba(240,192,176,0) 100%),
      radial-gradient(ellipse 260px 180px at 700px 520px, var(--rose) 0%, rgba(238,176,216,0) 100%),
      radial-gradient(ellipse 240px 200px at 560px 720px, var(--sky) 0%, rgba(169,200,246,0) 100%),
      linear-gradient(135deg, var(--lilac), var(--pink) 45%, var(--sky) 70%, var(--mauve-grey));
  }
  .shimmer-texture {
    position: absolute;
    inset: 0;
  }

  /* Back cover */
  .back-blurb {
    position: absolute;
    left: 90px;
    top: 283px;
    width: 312px;
    margin: 0;
    font-family: "Open Sans", sans-serif;
    font-size: 9.6px;
    line-height: 18.4px;
    color: var(--text-white);
    text-align: justify;
  }

  /* Spine */
  .spine-title,
  .spine-author {
    position: absolute;
    writing-mode: vertical-rl;
    margin: 0;
    white-space: nowrap;
  }
  .spine-title {
    left: 512px;
    top: 48px;
    font-family: "Archivo", sans-serif;
    font-weight: 700;
    font-size: 35px;
    letter-spacing: 0.14em;
    color: var(--text-white);
  }
  .spine-author {
    left: 517px;
    top: 527px;
    font-family: "Archivo", sans-serif;
    font-weight: 700;
    font-size: 21px;
    color: var(--spine-author-blue);
  }

  /* Front cover */
  .front-cover {
    position: absolute;
    left: 570px;
    top: 0;
    width: 488px;
    height: 787px;
    text-align: center;
  }
  .bestseller-line {
    position: absolute;
    left: 52px;
    top: 38px;
    width: 382px;
    margin: 0;
    padding-bottom: 5px;
    border-bottom: 1px solid var(--ink-black);
    font-family: "Tinos", serif;
    font-size: 19.5px;
    letter-spacing: 0.13em;
    color: var(--ink-black);
    white-space: nowrap;
  }
  .author-name {
    position: absolute;
    left: 0;
    top: 240px;
    width: 100%;
    margin: 0;
    font-family: "Archivo", sans-serif;
    font-weight: 700;
    font-size: 29px;
    letter-spacing: 0.03em;
    color: var(--ink-black);
  }
  .book-title {
    position: absolute;
    left: 0;
    top: 326px;
    width: 100%;
    margin: 0;
    font-family: "Archivo", sans-serif;
    font-weight: 800;
    font-size: 47px;
    letter-spacing: 0.12em;
    color: var(--title-violet);
  }
  .book-subtitle {
    position: absolute;
    left: 0;
    top: 673px;
    width: 100%;
    margin: 0;
    font-family: "Archivo", sans-serif;
    font-weight: 700;
    font-size: 27px;
    line-height: 36px;
    color: var(--ink-black);
  }
</style>
</head>
<body>
  <main class="cover-spread">
    <svg class="shimmer-texture" width="1058" height="787" viewBox="0 0 1058 787" aria-hidden="true">
      <defs>
        <linearGradient id="sheen" x1="0" y1="0" x2="1" y2="1">
          <stop offset="0" stop-color="#ffffff" stop-opacity="0"/>
          <stop offset="0.5" stop-color="#ffffff" stop-opacity="0.18"/>
          <stop offset="1" stop-color="#ffffff" stop-opacity="0"/>
        </linearGradient>
      </defs>
      <rect x="570" y="0" width="488" height="787" fill="url(#sheen)"/>
    </svg>

    <section class="back-cover">
      <p class="back-blurb">Lorem ipsum dolor sit amet, consectetur adipiscing elit, sed do eiusmod tempor incididunt ut labore et dolore magna aliqua. Quis ipsum suspendisse ultrices gravida. Risus commodo viverra maecenas accumsan lacus vel facilisis. Lorem ipsum dolor sit amet, consectetur adipiscing elit, sed do eiusmod tempor incididunt ut labore et dolore magna aliqua. Quis ipsum suspendisse ultrices gravida. Risus commodo viverra maecenas accumsan lacus vel facilisis. Lorem ipsum dolor sit amet, consectetur adipiscing elit, sed do eiusmod tempor incididunt ut labore et dolore magna aliqua. Quis ipsum suspendisse ultrices gravida. Risus commodo viverra maecenas accumsan lacus vel facilisis.</p>
    </section>

    <section class="spine">
      <p class="spine-title">UNWAVERING</p>
      <p class="spine-author">Carla Jean Morrow</p>
    </section>

    <section class="front-cover">
      <p class="bestseller-line">DAILY MERIDIAN BESTSELLER</p>
      <p class="author-name">Carla Jean Morrow</p>
      <h1 class="book-title">UNWAVERING</h1>
      <p class="book-subtitle">Ways to Kindle<br>the Spark of Resolve</p>
    </section>
  </main>
</body>
</html>
```